Veltrium stationery design

Design stationery for us that fits with the colours of the logo. We are looking for letterheads, business cards etc. Something we can use for a prospectus and marketing presentations in power point. Must be completed in such a manner that it represents a corporate image for large enterprise clients and other large organisations. The company is a project assurance and monitoring company that works in all industries.

```html
<!DOCTYPE html>
<html lang="en">
<head>
<meta charset="UTF-8">
<title>Veltrium Business Card</title>
<link href="https://fonts.googleapis.com/css2?family=Montserrat:wght@300;400;800&display=swap" rel="stylesheet">
<style>
  :root {
    --card-black: #131313;
    --card-black-soft: #1c1c1c;
    --brand-blue: #1d4fb3;
    --brand-blue-deep: #0f2f78;
    --brand-orange: #f2521c;
    --brand-orange-light: #ff7a1f;
    --text-light: #e8e8e8;
    --rule-light: #cfcfcf;
  }
  * { margin: 0; padding: 0; box-sizing: border-box; }
  html, body {
    width: 1200px;
    height: 686px;
    overflow: hidden;
    background: #ffffff;
  }
  .business-card {
    position: relative;
    width: 1200px;
    height: 686px;
    border-radius: 22px;
    overflow: hidden;
    background: radial-gradient(ellipse at 50% 40%, var(--card-black-soft) 0%, var(--card-black) 70%);
    font-family: "Montserrat", sans-serif;
  }
  .corner-accents {
    position: absolute;
    inset: 0;
    width: 1200px;
    height: 686px;
  }
  .brand-lockup {
    position: absolute;
    top: 240px;
    left: 0;
    width: 1200px;
    display: flex;
    align-items: center;
    justify-content: center;
    gap: 34px;
  }
  .brand-dot {
    width: 110px;
    height: 110px;
    border-radius: 50%;
    background: var(--brand-blue);
  }
  .brand-name {
    font-weight: 800;
    font-size: 84px;
    letter-spacing: 2px;
    color: var(--brand-orange);
    line-height: 1;
  }
  .tagline {
    position: absolute;
    top: 436px;
    left: 0;
    width: 1200px;
    display: flex;
    align-items: center;
    justify-content: center;
    gap: 22px;
    color: var(--text-light);
    font-weight: 400;
    font-size: 19px;
    letter-spacing: 3.6px;
  }
  .tagline-rule {
    width: 66px;
    height: 1.5px;
    background: var(--rule-light);
  }
  .website {
    position: absolute;
    top: 588px;
    left: 0;
    width: 1200px;
    display: flex;
    align-items: center;
    justify-content: center;
    gap: 28px;
    color: var(--text-light);
    font-weight: 400;
    font-size: 25px;
    letter-spacing: 2.4px;
  }
  .website-icon { width: 32px; height: 32px; }
</style>
</head>
<body>
  <div class="business-card">
    <svg class="corner-accents" viewBox="0 0 1200 686" aria-hidden="true">
      <defs>
        <linearGradient id="blueFade" x1="0" y1="0" x2="1" y2="1">
          <stop offset="0" stop-color="#1d4fb3"/>
          <stop offset="1" stop-color="#0f2f78"/>
        </linearGradient>
        <linearGradient id="orangeFade" x1="0" y1="0" x2="1" y2="1">
          <stop offset="0" stop-color="#ff7a1f"/>
          <stop offset="1" stop-color="#e0400f"/>
        </linearGradient>
      </defs>
      <!-- top right -->
      <polygon points="885,0 1200,0 1200,205" fill="url(#blueFade)"/>
      <line x1="880" y1="0" x2="1200" y2="208" stroke="var(--brand-orange)" stroke-width="4"/>
      <polygon points="1200,145 1108,208 1200,302" fill="url(#orangeFade)"/>
      <!-- bottom left -->
      <polygon points="0,422 0,686 270,686" fill="url(#blueFade)"/>
      <line x1="0" y1="414" x2="282" y2="686" stroke="var(--brand-orange)" stroke-width="4"/>
    </svg>

    <div class="brand-lockup">
      <div class="brand-dot"></div>
      <div class="brand-name">VELTRIUM</div>
    </div>

    <div class="tagline">
      <span class="tagline-rule"></span>
      <span class="tagline-text">DELIVERING EXCELLENCE. DRIVING FUTURES.</span>
      <span class="tagline-rule"></span>
    </div>

    <div class="website">
      <svg class="website-icon" viewBox="0 0 32 32" fill="none" stroke="var(--brand-blue)" stroke-width="2" aria-hidden="true">
        <circle cx="16" cy="16" r="13"/>
        <ellipse cx="16" cy="16" rx="6" ry="13"/>
        <line x1="3" y1="16" x2="29" y2="16"/>
        <line x1="5" y1="9" x2="27" y2="9"/>
        <line x1="5" y1="23" x2="27" y2="23"/>
      </svg>
      <span class="website-text">www.veltrium.com</span>
    </div>
  </div>
</body>
</html>
```